Real Estate Sales Window Card

We require a Window card for real estate sales and leasing.
K7 Residences is a wool store conversion located in the trendy, riverside suburb of Teneriffe, Brisbane. The clientele are generally professional couples working inner city jobs.
The card should reflect the style and colouring of the existing themes of the building, in particular the simple structural aspects with primary colours of black, white, grey, mocha and olive green.
For more details on the K7 residences please see http://k7residences.com.au/about/gallery/apartment-gallery (please note: disregard the red on the site as it is not part of the buildings tones)
The card should contain the following:
- Header
- Price
- Bed, Bath, Car
- Description
- Photo(s)
- Ad type (i.e. Sale or Lease)
The card will be used in A4 portrait and A3 landscape aspects.
Industry/Entity Type
Real Estate
Look and feel
Each slider illustrates characteristics of the customer's brand and the style your logo design should communicate.

```html
<!DOCTYPE html>
<html lang="en">
<head>
<meta charset="utf-8">
<title>K7 Residences – Window Card</title>
<link href="https://fonts.googleapis.com/css2?family=Open+Sans:wght@400;700&family=Questrial&display=swap" rel="stylesheet">
<style>
  :root {
    --page-bg: #d9d6d2;
    --charcoal: #2c2c2c;
    --charcoal-deep: #1f1f1f;
    --panel-grey: #c9c9c9;
    --box-white: #f2f2f2;
    --mocha: #6f5646;
    --mocha-light: #b8997e;
    --olive: #6d7244;
    --ink: #1c1c1c;
    --frame: #2e2e2e;
  }
  * { box-sizing: border-box; margin: 0; padding: 0; }
  html, body { width: 900px; height: 1200px; overflow: hidden; }
  body { background: var(--page-bg); font-family: "Questrial", "Century Gothic", sans-serif; color: var(--ink); }

  .card {
    position: absolute; left: 40px; top: 30px; width: 820px; height: 1140px;
    background: radial-gradient(ellipse at 50% 45%, #d8d8d8 0%, var(--panel-grey) 60%, #b4b4b4 100%);
    box-shadow: 0 10px 30px rgba(0,0,0,.35);
    overflow: hidden;
  }
  .masthead { position: absolute; left: 0; top: 0; width: 820px; height: 270px; background: var(--charcoal); }
  .brand {
    position: absolute; top: 28px; left: 0; width: 100%; text-align: center;
    font-family: "Open Sans", sans-serif; font-weight: 700; color: var(--mocha-light);
    font-size: 40px; letter-spacing: 1px; text-transform: uppercase;
  }
  .building-elevation {
    position: absolute; left: 40px; top: 100px; width: 740px; height: 160px;
    background: linear-gradient(180deg, #3a3a3a 0%, #4a4a4a 55%, #3c3c3c 100%);
  }

  .panel {
    position: absolute; background: var(--box-white);
    box-shadow: 0 14px 14px -8px rgba(0,0,0,.45);
  }
  .panel-title {
    position: absolute; left: 0; top: 0; right: 0; height: 30px;
    background: var(--mocha); color: #fff;
    font-family: "Questrial", sans-serif; font-weight: 400; font-size: 21px; line-height: 30px;
    padding-left: 42px;
    box-shadow: 0 3px 4px rgba(0,0,0,.3);
  }
  .panel-title svg { position: absolute; left: 10px; top: 3px; }

  .price { left: 50px; top: 300px; width: 270px; height: 205px; }
  .price-lines { position: absolute; left: 18px; top: 66px; font-size: 17px; line-height: 30px; }
  .price-lines .amount { color: var(--olive); }
  .ad-type {
    position: absolute; left: 18px; bottom: 18px;
    font-size: 13px; letter-spacing: 2px; text-transform: uppercase; color: var(--olive);
  }

  .features { left: 335px; top: 300px; width: 430px; height: 205px; }
  .features-body { position: absolute; left: 14px; top: 44px; right: 14px; font-size: 12px; line-height: 17px; }
  .features-body p + p { margin-top: 12px; }
  .label { color: var(--olive); }

  .description { left: 45px; top: 530px; width: 720px; height: 200px; }
  .description-body { position: absolute; left: 14px; top: 44px; right: 14px; font-size: 12.5px; line-height: 18px; }

  .photos { left: 40px; top: 760px; width: 730px; height: 240px; }
  .gallery { position: absolute; left: 22px; top: 50px; display: flex; gap: 14px; }
  .photo {
    width: 160px; height: 150px; border: 6px solid var(--frame);
    box-shadow: 0 14px 10px -6px rgba(0,0,0,.45);
  }
  .photo.lobby { background: linear-gradient(135deg, #d7d9da, #8a6a4e 70%, #4a3a2c); }
  .photo.terrace { background: linear-gradient(160deg, #9fb28a, #6e5a45 60%, #3b3128); }
  .photo.bathroom { background: linear-gradient(180deg, #f0f0ef, #d9d5cf 60%, #a58860); }
  .photo.timber { background: linear-gradient(120deg, #6b5a4c, #a29384 50%, #2d2824); }

  .footer-band { position: absolute; left: 0; bottom: 0; width: 820px; height: 90px; background: var(--charcoal-deep); }
</style>
</head>
<body>
<main class="card">
  <header class="masthead">
    <div class="brand">K7 Residences</div>
    <div class="building-elevation" role="img" aria-label="Line elevation drawing of the converted wool store building"></div>
  </header>

  <section class="panel price">
    <h2 class="panel-title">
      <svg width="24" height="24" viewBox="0 0 24 24"><path d="M3 12 L12 3 H21 V12 L12 21 Z" fill="#e9dfd3" stroke="#fff" stroke-width="1.5"/><circle cx="17" cy="7" r="1.8" fill="#6f5646"/></svg>
      Price
    </h2>
    <div class="price-lines">
      <p>The house Price is <span class="amount">1.800.000.00 $</span></p>
      <p>The Rent Price is &nbsp;&nbsp;<span class="amount">1.800 $</span></p>
    </div>
    <p class="ad-type">For Sale or Lease</p>
  </section>

  <section class="panel features">
    <h2 class="panel-title">
      <svg width="24" height="24" viewBox="0 0 24 24"><rect x="3" y="5" width="18" height="14" rx="2" fill="#fff"/><rect x="6" y="9" width="12" height="6" fill="#6d7244"/></svg>
      Bed, Bath, Car
    </h2>
    <div class="features-body">
      <p><span class="label">Amenities:</span> Attach Mstr Bath, Curved Stair, Double Vanities, Entry Lvl BR, MBA/Sep Shwr, MBA/Sep Tub, MBR-BA Full, Master Walk-in Closet, Shades/Blinds, W/W Carpeting</p>
      <p><span class="label">Appliances:</span> Central Vacuum, Dishwasher, Disposal, Dryer, Dryer-front loading, Exhaust Fan, Freezer, Icemaker, Microwave, Oven-Double, Oven-Wall, Oven/Range-Gas, Range hood, Six burner stove, Washer, Water Conditioner</p>
    </div>
  </section>

  <section class="panel description">
    <h2 class="panel-title">
      <svg width="26" height="24" viewBox="0 0 26 24"><path d="M2 12 L13 2 L24 12" fill="none" stroke="#fff" stroke-width="2.5"/><rect x="6" y="11" width="14" height="11" fill="#fff"/><rect x="11" y="15" width="4" height="7" fill="#6d7244"/></svg>
      Description
    </h2>
    <div class="description-body">
      <p>Perfect blend of formal elegance and casual Bayhaven lifestyle. Custom built 6BR/5.5BA on prime 6.24 waterfront acres in Heron Bend Farm. Formal LR &amp; DR, gourmet kitchen with family room overlooking pool and pool house. Separate 8 stall garage with private office and 2BR/2BA guest house. 1600 linear feet of perfectly wrapped shoreline. 196' pier and 2 separate boat houses. Perfect blend of formal elegance and casual Bayhaven lifestyle. Custom built 6BR/5.5BA on prime 6.24 waterfront acres in Heron Bend Farm. Formal LR &amp; DR, gourmet kitchen with family room overlooking pool and pool house. Separate 8 stall garage with private office and 2BR/2BA guest house. 1600 linear feet of perfectly wrapped shoreline. 196' pier and 2 separate boat houses.</p>
    </div>
  </section>

  <section class="panel photos">
    <h2 class="panel-title">
      <svg width="26" height="24" viewBox="0 0 26 24"><rect x="2" y="6" width="22" height="15" rx="2" fill="none" stroke="#fff" stroke-width="2"/><rect x="8" y="3" width="8" height="4" fill="#fff"/><circle cx="13" cy="13.5" r="4.5" fill="none" stroke="#fff" stroke-width="2"/></svg>
      Photos
    </h2>
    <div class="gallery">
      <div class="photo lobby" role="img" aria-label="Photo of an open living area with timber and glass"></div>
      <div class="photo terrace" role="img" aria-label="Photo of a potted plant on a timber terrace"></div>
      <div class="photo bathroom" role="img" aria-label="Photo of a white basin on a timber bench"></div>
      <div class="photo timber" role="img" aria-label="Photo of timber structural detail"></div>
    </div>
  </section>

  <footer class="footer-band"></footer>
</main>
</body>
</html>
```